Emergency Medical Training and Events Company Business Needs Business Card Design

We are in need of a business card for our dynamic company expanding its customer base and need to be easily contacted and identified for when we visit with government officials, potential EMS / Fire agencies and county coordinators to arrange for training programs for first responders to better prepare them for critical thinking at critical incidents.

Target Market(s)

EMS/Fire and Event Promoters

Industry/Entity Type

Medical

Contact Information for Business Card

Two cards, comparable designs:

Martin K. Halvey, Principal, m.halvey@rvqtlo.com
Owen Tash, Event and Training Specialist, o.tash@rvqtlo.com

Font styles to use
Other font styles liked:
• Cambria

Colors

Designer to choose colors to be used in the design.

Requirements
Must have
• Company Logo, Spots for Name, Title, Phone Number, Email, Website
• A bullet list stating that we offer, QRB CPR and First Aid Instructors, Hold the Line Instructors, Event EMS, CME's, MCI Training and Planning. We prefer to have a black background for the card but if you can make a blue or white card stand out we would review that as well.
Should not have
• Tacky logos or special sayings ... simple, elegant, professional is the look we seek

```html
<!DOCTYPE html>
<html lang="en">
<head>
<meta charset="utf-8">
<title>Rvqtlo Solutions – Business Cards</title>
<link rel="stylesheet" href="https://fonts.googleapis.com/css2?family=Noto+Serif:wght@400;700&display=swap">
<style>
  :root {
    --page: #ffffff;
    --navy: #1b1f4d;
    --red: #c21715;
    --white: #ffffff;
    --shadow: rgba(0, 0, 0, 0.45);
  }
  * { margin: 0; padding: 0; box-sizing: border-box; }
  html, body {
    width: 1200px; height: 716px; overflow: hidden;
    background: var(--page);
    font-family: "Noto Serif", Cambria, Georgia, serif;
  }
  .sheet { position: relative; width: 1200px; height: 716px; }

  .card {
    position: absolute;
    width: 487px; height: 293px;
    background: var(--navy);
    border-radius: 20px;
    overflow: hidden;
    box-shadow: 4px 6px 7px var(--shadow);
  }
  .card::after {
    content: ""; position: absolute; left: 0; right: 0; bottom: 0;
    height: 16px; background: var(--red);
  }
  .card--top-left { left: 97px; top: 50px; }
  .card--top-right { left: 629px; top: 50px; }
  .card--bottom-left { left: 97px; top: 371px; }
  .card--bottom-right { left: 629px; top: 371px; }

  .person-name {
    position: absolute; left: 41px; top: 46px;
    color: var(--white); font-weight: 700; font-size: 36px; line-height: 1.2;
    white-space: nowrap;
  }
  .person-title {
    position: absolute; left: 42px; top: 85px;
    color: var(--red); font-weight: 400; font-size: 19px; line-height: 1.2;
    white-space: nowrap;
  }
  .contact-list { position: absolute; left: 41px; top: 148px; list-style: none; }
  .contact-item {
    display: flex; align-items: center; height: 22px; margin-bottom: 10px;
    color: var(--white); font-size: 15.5px; letter-spacing: 0.4px; white-space: nowrap;
  }
  .contact-icon { width: 19px; height: 19px; margin-right: 11px; flex: none; }

  .brand-mark { position: absolute; border-radius: 50%; background: var(--red); }
  .brand-mark--front { left: 341px; top: 75px; width: 90px; height: 90px; }
  .brand-mark--back { left: 46px; top: 101px; width: 90px; height: 90px; }

  .brand-rule { position: absolute; left: 329px; top: 168px; width: 114px; height: 2px; background: var(--red); }
  .brand-divider { position: absolute; left: 141px; top: 114px; width: 2px; height: 63px; background: var(--red); }

  .brand-name {
    position: absolute; color: var(--white); font-weight: 700; white-space: nowrap;
  }
  .brand-name span { display: block; }
  .brand-name--front { left: 329px; top: 170px; width: 114px; text-align: center; }
  .brand-name--front .brand-main { font-size: 25px; line-height: 30px; letter-spacing: 1px; }
  .brand-name--front .brand-sub { font-size: 13px; line-height: 15px; letter-spacing: 0.6px; }
  .brand-name--back { left: 152px; top: 108px; }
  .brand-name--back .brand-main { font-size: 42px; line-height: 50px; letter-spacing: 2px; }
  .brand-name--back .brand-sub { font-size: 21px; line-height: 22px; letter-spacing: 3.4px; }
</style>
</head>
<body>
<main class="sheet">

  <section class="card card--top-left" aria-label="Front card, Martin K. Halvey">
    <h1 class="person-name">Martin K. Halvey</h1>
    <p class="person-title">Principal</p>
    <ul class="contact-list">
      <li class="contact-item">
        <svg class="contact-icon" viewBox="0 0 20 20" aria-hidden="true"><circle cx="10" cy="10" r="10" fill="#c21715"/><path d="M6.3 5.2l2 -0.4 1.2 2.6-1.3 1c.6 1.3 1.5 2.3 2.8 2.9l1-1.3 2.6 1.2-.4 2c-4.6.2-8.2-3.4-7.9-8z" fill="#1b1f4d"/></svg>
        555.014.2286
      </li>
      <li class="contact-item">
        <svg class="contact-icon" viewBox="0 0 20 20" aria-hidden="true"><circle cx="10" cy="10" r="10" fill="#c21715"/><rect x="5" y="6.5" width="10" height="7" fill="none" stroke="#1b1f4d" stroke-width="1"/><path d="M5 6.5l5 4 5-4M5 13.5l3.6-3.5M15 13.5l-3.6-3.5" fill="none" stroke="#1b1f4d" stroke-width="1"/></svg>
        m.halvey@rvqtlo.com
      </li>
      <li class="contact-item">
        <svg class="contact-icon" viewBox="0 0 20 20" aria-hidden="true"><circle cx="10" cy="10" r="10" fill="#c21715"/><g fill="none" stroke="#1b1f4d" stroke-width="1"><circle cx="10" cy="10" r="5.5"/><ellipse cx="10" cy="10" rx="2.4" ry="5.5"/><path d="M4.5 10h11M5.3 7.3h9.4M5.3 12.7h9.4"/></g></svg>
        www.rvqtlo.com
      </li>
    </ul>
    <span class="brand-mark brand-mark--front"></span>
    <span class="brand-rule"></span>
    <p class="brand-name brand-name--front"><span class="brand-main">RVQTLO</span><span class="brand-sub">SOLUTIONS</span></p>
  </section>

  <section class="card card--top-right" aria-label="Front card, Owen Tash">
    <h1 class="person-name">Owen Tash</h1>
    <p class="person-title">Event and Training Specialist</p>
    <ul class="contact-list">
      <li class="contact-item">
        <svg class="contact-icon" viewBox="0 0 20 20" aria-hidden="true"><circle cx="10" cy="10" r="10" fill="#c21715"/><path d="M6.3 5.2l2 -0.4 1.2 2.6-1.3 1c.6 1.3 1.5 2.3 2.8 2.9l1-1.3 2.6 1.2-.4 2c-4.6.2-8.2-3.4-7.9-8z" fill="#1b1f4d"/></svg>
        555.017.4410
      </li>
      <li class="contact-item">
        <svg class="contact-icon" viewBox="0 0 20 20" aria-hidden="true"><circle cx="10" cy="10" r="10" fill="#c21715"/><rect x="5" y="6.5" width="10" height="7" fill="none" stroke="#1b1f4d" stroke-width="1"/><path d="M5 6.5l5 4 5-4M5 13.5l3.6-3.5M15 13.5l-3.6-3.5" fill="none" stroke="#1b1f4d" stroke-width="1"/></svg>
        o.tash@rvqtlo.com
      </li>
      <li class="contact-item">
        <svg class="contact-icon" viewBox="0 0 20 20" aria-hidden="true"><circle cx="10" cy="10" r="10" fill="#c21715"/><g fill="none" stroke="#1b1f4d" stroke-width="1"><circle cx="10" cy="10" r="5.5"/><ellipse cx="10" cy="10" rx="2.4" ry="5.5"/><path d="M4.5 10h11M5.3 7.3h9.4M5.3 12.7h9.4"/></g></svg>
        www.rvqtlo.com
      </li>
    </ul>
    <span class="brand-mark brand-mark--front"></span>
    <span class="brand-rule"></span>
    <p class="brand-name brand-name--front"><span class="brand-main">RVQTLO</span><span class="brand-sub">SOLUTIONS</span></p>
  </section>

  <section class="card card--bottom-left" aria-label="Back card">
    <span class="brand-mark brand-mark--back"></span>
    <span class="brand-divider"></span>
    <p class="brand-name brand-name--back"><span class="brand-main">RVQTLO</span><span class="brand-sub">SOLUTIONS</span></p>
  </section>

  <section class="card card--bottom-right" aria-label="Back card">
    <span class="brand-mark brand-mark--back"></span>
    <span class="brand-divider"></span>
    <p class="brand-name brand-name--back"><span class="brand-main">RVQTLO</span><span class="brand-sub">SOLUTIONS</span></p>
  </section>

</main>
</body>
</html>
```